Logo-Design für Oldtimerhandel Wendtner&Wendtner klassische Automobile OG
Zielgruppe
Handel mit Oldtimern, speziell aus den 60er und 70er Jahren. Zielgruppe sind überwiegend Menschen, die sich von der Masse abheben möchten und Wert auf etwas Einzigartiges legen.
Aufgabenstellung
Das Design soll ein hochwertiges Gesamterscheinungsbild mit gutem Wiedererkennungswert haben. Auch kann ein stilisierter Oldtimer Teil des Logos sein, um für die Zielgruppe besser erkennbar zu sein.
Das Logo muss für Homepage, Visitkarten, Briefpapier etc. tauglich sein und auch in S/W gut erkennbar sein können. Ebenso sollte es möglich sein, Autos mit dem Logo bzw. Schriftzug zu branden.
Beispielhaft wäre das Logo bzw. der Internetauftritt von http://www.moravek-vintage-motors.com vergleichbar.

```html
<!DOCTYPE html>
<html lang="de">
<head>
<meta charset="utf-8">
<title>Wendtner &amp; Wendtner – Geschäftsausstattung</title>
<link href="https://fonts.googleapis.com/css2?family=Questrial&display=swap" rel="stylesheet">
<style>
:root{
  --red:#c8161d;
  --grey:#8c8c8c;
  --ink:#222;
  --paper:#fff;
  --stage:#f1f1f1;
  --window:#aaa;
}
*{margin:0;padding:0;box-sizing:border-box}
html,body{width:1200px;height:801px;overflow:hidden}
body{background:var(--stage);font-family:"Questrial",sans-serif;color:var(--ink);position:relative}
.sheet{position:absolute;background:var(--paper);box-shadow:0 4px 10px rgba(0,0,0,.12)}
.wordmark{color:var(--red);font-weight:400;line-height:.95;letter-spacing:-.01em;text-transform:uppercase;display:flex;align-items:center;gap:.35em}
.wordmark .dot{width:.9em;height:.9em;background:var(--red);flex:none}
.wordmark .lines span{display:block}

.hero-logo{position:absolute;left:169px;top:72px;font-size:36px}
.label{position:absolute;top:224px;font-size:16px;color:#777;width:260px;text-align:center}
.label--front{left:58px}.label--back{left:333px}

.card--front{left:58px;top:254px;width:259px;height:167px;display:flex;align-items:center;justify-content:center}
.card--front .wordmark{font-size:19px}
.card--back{left:333px;top:254px;width:260px;height:168px;padding:38px 0 0 30px}
.card--back .square{position:absolute;left:30px;top:40px;width:26px;height:26px;background:var(--red)}
.card--back .info{margin-left:38px;font-size:8.6px;color:var(--grey);line-height:1.35}
.card--back .name{font-size:15px;color:var(--red);margin-bottom:4px}
.card--back .gap{height:7px}

.envelope{left:58px;top:496px;width:537px;height:267px}
.envelope .wordmark{position:absolute;left:45px;top:32px;font-size:19px}
.envelope .window{position:absolute;left:47px;top:121px;width:206px;height:111px;border-radius:12px;background:linear-gradient(135deg,#a3a3a3,#bdbdbd)}

.letter{left:630px;top:34px;width:521px;height:737px;font-size:7.4px}
.letter .wordmark{position:absolute;right:32px;top:30px;font-size:15px}
.sender{position:absolute;right:32px;top:103px;text-align:right;color:var(--grey);font-size:6.3px;line-height:1.65}
.sender .firm{color:var(--red)}
.sender .gap{height:7px}
.return-line{position:absolute;left:62px;top:156px;font-size:5.4px;color:var(--red)}
.recipient{position:absolute;left:62px;top:166px;line-height:1.65}
.subject{position:absolute;left:62px;top:245px;font-size:7.8px;font-weight:700}
.body{position:absolute;left:62px;top:276px;width:423px;line-height:1.42}
.body p{margin-bottom:10px}
.fold{position:absolute;left:0;width:10px;height:1px;background:#666}
.footer{position:absolute;top:686px;font-size:6px;color:var(--grey);line-height:1.75}
.footer .firm{font-weight:700}
</style>
</head>
<body>

<div class="wordmark hero-logo"><span class="dot"></span><div class="lines"><span>Wendtner</span><span>&amp; Wendtner</span><span>Oldtimerhandel</span></div></div>

<div class="label label--front">Visitenkarte vorne</div>
<div class="label label--back">Visitenkarte hinten</div>

<div class="sheet card--front">
  <div class="wordmark"><span class="dot"></span><div class="lines"><span>Wendtner</span><span>&amp; Wendtner</span><span>Oldtimerhandel</span></div></div>
</div>

<div class="sheet card--back">
  <span class="square"></span>
  <div class="info">
    <div class="name">Max Mustermann</div>
    Musterstraße 123<br>12345 Musterstadt<br>Tel.: 01234 567891
    <div class="gap"></div>
    musteremail@wendtnerundwendtner.de<br>www.wendtnerundwendtner.de
  </div>
</div>

<div class="sheet envelope">
  <div class="wordmark"><span class="dot"></span><div class="lines"><span>Wendtner</span><span>&amp; Wendtner</span><span>Oldtimerhandel</span></div></div>
  <div class="window"></div>
</div>

<div class="sheet letter">
  <div class="wordmark"><span class="dot"></span><div class="lines"><span>Wendtner</span><span>&amp; Wendtner</span><span>Oldtimerhandel</span></div></div>

  <div class="sender">
    <div class="firm">WENDTNER &amp; WENDTNER</div>
    <div class="firm">Oldtimerhandel</div>
    Musterstraße 123<br>12345 Musterstadt
    <div class="gap"></div>
    Telefon: 01234 567891<br>Telefax: 01234 567812
    <div class="gap"></div>
    info@wendtnerundwendtner.de<br>www.wendtnerundwendtner.de
  </div>

  <div class="return-line">WENDTNER &amp; WENDTNER | Musterstraße 123 | 12345 Musterstadt</div>
  <div class="recipient">Frau Musterbeispiel<br>Musterstraße 3<br>48555 Muster</div>

  <div class="subject">Hier steht eine Betreffzeile</div>

  <div class="body">
    <p>Sehr geehrte Frau Musterbeispiel,</p>
    <p>als Kunde unseres jungen und modernen Unternehmens erwartet<br>Sie Qualität in höchstem Maße.</p>
    <p>Sie können sicher zu sein, genau zu bekommen, was wir Ihnen versprechen.<br>Und damit werden Sie auch rundum zufrieden sein. Das garantieren wir Ihnen.</p>
    <p>Schauen Sie doch gleich das beiliegende Prospekt. Wir bieten Ihnen moderne und hochwertige Produkte, die auf dem neuesten Stand der Technik sind, an. Überzeugen Sie sich selbst von der hochwertigen Qualität unserer Produkte und bestellen Sie noch heute.</p>
    <p>Wir freuen uns auf Ihre Bestellung und sind bei Rückfragen gerne für Sie da.</p>
    <p>Mit freundlichen Grüßen</p>
  </div>

  <span class="fold" style="top:260px"></span>
  <span class="fold" style="top:368px"></span>
  <span class="fold" style="top:520px"></span>

  <div class="footer" style="left:54px"><span class="firm">WENDTNER &amp; WENDTNER</span><br>Musterstraße 123<br>12345 Musterstadt</div>
  <div class="footer" style="left:146px">USt-IDNR: DE1234567<br>Steuernummer: 111/222/333<br>Inhaber: Max Mustermann</div>
  <div class="footer" style="left:253px">Musterbank Musterstadt<br>IBAN: DE00 1234 5678 9000 0000<br>BIC: MUSTDEXX00</div>
</div>

</body>
</html>
```